I am a new company with the latest technology in the concrete polishing business

We need a logo design for a new company out of Toronto, Canada. We polish residential, commercial and industrial concrete as well as different epoxy toppings.

Target Market(s)

How Owners with expendable incomes

Industry/Entity Type

Construction

Contact Information for Business Card

be able to see content rather easily

Colors
0355a3
fbed22
1b1b1b

Requirements
Must have
• simple and elegant

```html
<!DOCTYPE html>
<html lang="en">
<head>
<meta charset="utf-8">
<title>Slabline Coatings — Business Card</title>
<link rel="stylesheet" href="https://fonts.googleapis.com/css2?family=Lato:wght@400;700;900&family=Roboto:wght@700&display=swap">
<style>
  :root {
    --brand-blue: #0355a3;
    --brand-yellow: #fbed22;
    --brand-black: #1b1b1b;
    --paper: #ffffff;
    --stage: #9a9a9a;
    --ink: #222222;
  }
  * { box-sizing: border-box; margin: 0; padding: 0; }
  html, body { width: 1200px; height: 900px; overflow: hidden; }
  body { background: var(--stage); position: relative; font-family: "Lato", sans-serif; color: var(--ink); }

  .card { position: absolute; top: 306px; height: 272px; box-shadow: 2px 3px 5px rgba(0,0,0,0.45); overflow: hidden; }
  .card--front { left: 149px; width: 439px; background: var(--paper); }
  .card--back { left: 608px; width: 441px; background: var(--brand-black); }

  .name-flag { position: absolute; left: 0; top: 26px; }
  .holder { position: absolute; left: 34px; top: 31px; }
  .holder__name { font-family: "Roboto", sans-serif; font-weight: 700; font-size: 16px; letter-spacing: 0.2px; color: var(--brand-blue); line-height: 18px; }
  .holder__name span { color: var(--brand-yellow); }
  .holder__role { font-size: 12.5px; line-height: 16px; color: var(--ink); }

  .brand { position: absolute; display: flex; flex-direction: column; align-items: center; }
  .brand__mark { background: var(--brand-blue); border: 2px solid var(--brand-yellow); }
  .brand__name { font-family: "Lato", sans-serif; font-weight: 900; white-space: nowrap; letter-spacing: -0.3px; }
  .card--front .brand { left: 213px; top: 60px; width: 204px; }
  .card--front .brand__mark { width: 70px; height: 65px; margin-bottom: 14px; }
  .card--front .brand__name { font-size: 23px; color: var(--brand-blue); }
  .card--back .brand { left: 104px; top: 76px; width: 234px; }
  .card--back .brand__mark { width: 82px; height: 75px; margin-bottom: 16px; }
  .card--back .brand__name { font-size: 26px; color: var(--brand-yellow); }

  .contact { position: absolute; left: 23px; top: 190px; list-style: none; font-size: 12.5px; line-height: 16px; }
  .contact li { display: flex; align-items: center; gap: 3px; }
  .contact svg { width: 10px; height: 10px; fill: var(--brand-blue); }

  .address { position: absolute; right: 23px; top: 206px; text-align: right; font-size: 12.5px; line-height: 16px; }

  .footer-band { position: absolute; left: 0; bottom: 0; }
</style>
</head>
<body>

<section class="card card--front">
  <svg class="name-flag" width="30" height="38" viewBox="0 0 30 38">
    <polygon points="0,0 10,0 13,38 0,38" fill="var(--brand-yellow)"/>
    <polygon points="11,0 29,0 29,38 14,38" fill="var(--brand-blue)"/>
  </svg>
  <div class="holder">
    <p class="holder__name">MARCUS <span>HALE</span></p>
    <p class="holder__role">Managing Director</p>
  </div>

  <div class="brand">
    <div class="brand__mark"></div>
    <p class="brand__name">Slabline Coatings</p>
  </div>

  <ul class="contact">
    <li><svg viewBox="0 0 10 10"><path d="M1 3.5C1 2 2.5 1.5 5 1.5S9 2 9 3.5L7.5 4.3 6.8 3.2H3.2L2.5 4.3zM2.5 5h5l1 3.5h-7z"/></svg>444 555 6688</li>
    <li><svg viewBox="0 0 10 10"><path d="M0.5 2h9v6.5h-9zM1.2 2.6 5 5.6 8.8 2.6" stroke="#fff" stroke-width="0.8"/></svg>info@youremail.com</li>
    <li><svg viewBox="0 0 10 10"><circle cx="5" cy="5" r="4.5"/><path d="M3 3.5 5 3 5.5 5 4 6.5M6.5 6.5 7.5 5" stroke="#fff" stroke-width="0.9" fill="none"/></svg>www.websitename.com</li>
  </ul>

  <p class="address">421, Address line here<br>Country Name,45452</p>

  <svg class="footer-band" width="439" height="20" viewBox="0 0 439 20">
    <polygon points="0,5 206,5 194,20 0,20" fill="var(--brand-yellow)"/>
    <polygon points="214,0 439,0 439,20 196,20" fill="var(--brand-blue)"/>
  </svg>
</section>

<section class="card card--back">
  <div class="brand">
    <div class="brand__mark"></div>
    <p class="brand__name">Slabline Coatings</p>
  </div>
</section>

</body>
</html>
```